Single Page/Scrolling Design for Model Recruitment site

We need a design (and if you are capable, coding) for our company, Brimwell Parlour (LA as in Los Angeles). We like modern single page designs, hence the title for the project. We have already had a designer come up with a logo, which is attached. You're free to play around with the colors, although we want the site to have a feminine appeal to it.

The site is basically a recruitment project for girls who are interested in working as chat hosts for cam sites. We don't want anything cheesy that feels like a porn site. The inspiration for the logo (and the inspiration for the site) comes from the French and English salons of the late 18th century, where beautiful and intelligent women would gather to discuss a range of topics. We want the website to convey that this work is fun and exciting. Please keep these things in mind for the design.

As I mentioned, we like the modern look and feel of single page designs, especially because we don't have a ton of content. We just need an "About us" area, a "Work from Home" area, a "Work at The Brimwell Parlour" area, and "Contact Us" area which should have text boxes for entering email, subject, a message, etc.

The logo I mentioned is attached, as well as a very crude mockup of the layout of all the content I described.

Target Market(s)

Women age 18-35.

Industry/Entity Type

It Company

Font styles to use
Serif
Decorative
Script

Colors

Designer to choose colors to be used in the design.

Requirements
Should not have
• Images that are super sexual or even slightly pornographic. We want this to appeal to a broad range of women.

```html
<!DOCTYPE html>
<html lang="en">
<head>
<meta charset="utf-8">
<title>Brimwell Parlour — Chat Hosting</title>
<link rel="stylesheet" href="https://fonts.googleapis.com/css2?family=Raleway:wght@300;400;500;700;800&display=swap">
<style>
  :root {
    --pink: #e6198a;
    --bar: #2b2b2b;
    --nav-text: #b9b9b9;
    --ink: #333333;
    --muted: #8a8a8a;
    --body: #6f6f6f;
    --white: #ffffff;
    --hero-dark: #1a0d05;
    --hero-warm: #a9672e;
  }
  * { margin: 0; padding: 0; box-sizing: border-box; }
  html, body { width: 1079px; height: 1200px; overflow: hidden; background: var(--white); }
  body { position: relative; font-family: 'Raleway', sans-serif; color: var(--body); }

  .site-header { position: absolute; left: 0; top: 0; width: 1079px; height: 75px; background: var(--bar); }
  .brand { position: absolute; left: 70px; top: 26px; display: flex; align-items: center; gap: 7px;
    color: var(--pink); font-weight: 700; font-size: 14px; letter-spacing: 0.5px; }
  .brand-dot { width: 14px; height: 14px; border-radius: 50%; background: var(--pink); }
  .main-nav { position: absolute; right: 92px; top: 31px; display: flex; gap: 26px; list-style: none; }
  .main-nav li { font-size: 11px; letter-spacing: 2.6px; color: var(--nav-text); font-weight: 500; }
  .main-nav li.is-active { color: var(--pink); }

  .hero { position: absolute; left: 0; top: 75px; width: 1079px; height: 458px; overflow: hidden; }
  .hero-photo { position: absolute; inset: 0;
    background: radial-gradient(ellipse at 30% 30%, #c98a4e 0%, var(--hero-warm) 30%, #5a3016 65%, var(--hero-dark) 100%); }
  .hero-badge { position: absolute; left: 0; width: 100%; top: 90px; display: flex; justify-content: center; align-items: center; gap: 10px;
    color: var(--pink); font-weight: 700; font-size: 22px; line-height: 30px; }
  .hero-badge .brand-dot { width: 24px; height: 24px; }
  .hero-title { position: absolute; left: 0; width: 100%; top: 160px; text-align: center; color: var(--white);
    font-size: 88px; line-height: 1; letter-spacing: -1px; }
  .hero-title .light { font-weight: 300; }
  .hero-title .bold { font-weight: 800; }
  .hero-sub { position: absolute; left: 0; width: 100%; top: 251px; text-align: center; color: var(--pink);
    font-weight: 800; font-size: 15px; line-height: 20px; letter-spacing: -0.3px; }
  .hero-rule { position: absolute; top: 261px; height: 1px; width: 186px; background: #e8d8c8; }
  .hero-rule.left { left: 167px; }
  .hero-rule.right { left: 724px; }
  .hero-cta { position: absolute; left: 468px; top: 299px; width: 141px; height: 47px; border: 1px solid var(--white);
    color: var(--white); font-size: 15px; display: flex; align-items: center; justify-content: center; }
  .hero-down { position: absolute; left: 515px; top: 368px; }
  .hero-arrow { position: absolute; top: 187px; }
  .hero-arrow.prev { left: 11px; }
  .hero-arrow.next { left: 995px; }

  .about-title { position: absolute; left: 0; width: 100%; top: 602px; text-align: center; color: var(--ink);
    font-weight: 300; font-size: 34px; letter-spacing: 0.5px; }
  .about-divider { position: absolute; left: 505px; top: 652px; }
  .about-intro { position: absolute; left: 274px; width: 530px; top: 676px; text-align: center; color: var(--muted);
    font-size: 15.4px; line-height: 22px; }
  .about-copy { position: absolute; left: 90px; width: 420px; top: 802px; font-size: 13.7px; line-height: 28px; font-weight: 300; color: var(--body); }
  .about-copy p + p { margin-top: 25px; }
  .about-copy em { font-style: normal; color: var(--pink); font-weight: 400; }
  .about-cta { position: absolute; left: 90px; top: 1041px; width: 184px; height: 51px; border: 1px solid var(--ink);
    color: var(--ink); font-size: 15px; display: flex; align-items: center; justify-content: center; }
  .about-photo { position: absolute; left: 597px; top: 795px; width: 418px; height: 306px;
    background: linear-gradient(160deg, #d9d4d0 0%, #b9a99d 40%, #ece9ec 70%, #f4f2f6 100%); }
</style>
</head>
<body>
  <header class="site-header">
    <div class="brand"><span class="brand-dot"></span>Brimwell Parlour</div>
    <ul class="main-nav">
      <li class="is-active">HOME</li>
      <li>ABOUT</li>
      <li>TRAIN @ THE BRIMWELL PARLOUR</li>
      <li>WORK FROM HOME</li>
      <li>CONTACT</li>
    </ul>
  </header>

  <section class="hero">
    <div class="hero-photo" role="img" aria-label="Warm-toned close-up photograph in a dotted garment"></div>
    <div class="hero-badge"><span class="brand-dot"></span>Brimwell Parlour</div>
    <h1 class="hero-title"><span class="light">CHAT </span><span class="bold">HOSTING</span></h1>
    <span class="hero-rule left"></span>
    <span class="hero-rule right"></span>
    <p class="hero-sub">WELCOME TO THE BRIMWELL PARLOUR</p>
    <div class="hero-cta">START NOW!</div>
    <svg class="hero-down" width="48" height="48" viewBox="0 0 48 48">
      <circle cx="24" cy="24" r="23" fill="#1e1209"/>
      <path d="M19 22 L24 27 L29 22" fill="none" stroke="#fff" stroke-width="2.5"/>
    </svg>
    <svg class="hero-arrow prev" width="70" height="70" viewBox="0 0 70 70">
      <circle cx="35" cy="35" r="33" fill="none" stroke="#eadccf" stroke-width="2"/>
      <path d="M40 26 L28 35 L40 44 Z" fill="#eadccf"/>
    </svg>
    <svg class="hero-arrow next" width="70" height="70" viewBox="0 0 70 70">
      <circle cx="35" cy="35" r="33" fill="none" stroke="#eadccf" stroke-width="2"/>
      <path d="M30 26 L42 35 L30 44 Z" fill="#eadccf"/>
    </svg>
  </section>

  <section class="about">
    <h2 class="about-title">ABOUT US</h2>
    <svg class="about-divider" width="70" height="12" viewBox="0 0 70 12">
      <g fill="none" stroke="#e6198a" stroke-width="1">
        <path d="M6 1 L11 6 L6 11 L1 6 Z"/>
        <path d="M27 1 L32 6 L27 11 L22 6 Z"/>
        <path d="M48 1 L53 6 L48 11 L43 6 Z"/>
        <path d="M64 1 L69 6 L64 11 L59 6 Z"/>
      </g>
    </svg>
    <p class="about-intro">The Brimwell Parlour was started with the understanding that there is a large number of women sho are curious about working in webcam intertainment but have no idea where to start.</p>
    <div class="about-copy">
      <p>There are hundreds of <em>"studios" or "agencies"</em> on the internet with the goal of making money just by getting you to sign up, or even worse, by <em>taking a percentage of your comissions</em> once you do.</p>
      <p>That is not what <em>The Brimwell Parlour</em> is about. We want to be the premier destination for webcam entertainers to further their careers, <em>no matter</em> what level of experiece you have.</p>
    </div>
    <div class="about-cta">START NOW!</div>
    <div class="about-photo" role="img" aria-label="Photograph of a woman resting on white bedding by a sunlit window"></div>
  </section>
</body>
</html>
```